Real Estate Agent needs business card design

We have logo designed already, want to have business card designed. Very interested in those smaller size business card as they look very trendy. Business name is called VORENDA REALTY

```html
<!DOCTYPE html>
<html lang="en">
<head>
<meta charset="utf-8">
<title>Vorenda Realty – Business Card</title>
<link href="https://fonts.googleapis.com/css2?family=Merriweather:wght@400;700&display=swap" rel="stylesheet">
<style>
  :root {
    --page-bg: #ece7de;
    --card-white: #fbfaf7;
    --gold: #c8b287;
    --gold-light: #d9c7a0;
    --gold-deep: #b39a6a;
    --gold-text: #c2a36b;
    --ink: #3b352c;
    --on-gold: #4a3f2e;
    --white: #ffffff;
  }
  * { box-sizing: border-box; margin: 0; padding: 0; }
  html, body {
    width: 1200px; height: 780px; overflow: hidden;
    background: var(--page-bg);
    font-family: "Merriweather", Georgia, serif;
  }
  .sheet {
    width: 1200px; height: 780px;
    display: flex; align-items: center; justify-content: center; gap: 40px;
  }
  .card {
    position: relative;
    width: 540px; height: 330px;
    overflow: hidden;
    box-shadow: 0 6px 18px rgba(60, 45, 20, 0.18);
  }

  /* Front */
  .card-front { background: var(--card-white); }
  .front-band {
    position: absolute; left: 0; right: 0; top: 185px; bottom: 0;
    background: linear-gradient(180deg, var(--gold-light) 0%, var(--gold) 100%);
  }
  .social-square {
    position: absolute; top: 16px; right: 16px;
    width: 24px; height: 24px; border-radius: 3px;
    background: var(--gold);
  }
  .agent {
    position: absolute; left: 30px; top: 112px;
  }
  .agent-name {
    font-size: 22px; font-weight: 400; color: var(--gold-text);
    line-height: 1.2;
  }
  .agent-title {
    font-size: 12.5px; color: var(--ink); margin-top: 3px;
  }
  .brand-seal {
    position: absolute; left: 50%; top: 185px;
    width: 150px; height: 150px; margin: -75px 0 0 -75px;
    border-radius: 50%;
    background: var(--gold);
    border: 5px solid var(--white);
    display: flex; align-items: center; justify-content: center;
  }
  .brand-seal-name {
    font-size: 11px; letter-spacing: 1.5px; color: var(--white);
    text-align: center; line-height: 1.5;
  }
  .office-address {
    position: absolute; right: 26px; top: 208px;
    text-align: right; font-size: 12.5px; line-height: 1.6; color: var(--on-gold);
  }
  .contact-list {
    position: absolute; left: 30px; bottom: 20px;
    list-style: none; font-size: 12.5px; line-height: 1.6; color: var(--on-gold);
  }
  .contact-list li { display: flex; align-items: center; gap: 8px; }
  .contact-icon {
    width: 14px; height: 14px; border-radius: 50%;
    background: var(--white); opacity: .85; flex: none;
  }

  /* Back */
  .card-back {
    background: linear-gradient(160deg, var(--gold-light) 0%, var(--gold) 55%, var(--gold-deep) 100%);
    display: flex; align-items: center; justify-content: center; gap: 14px;
  }
  .back-mark {
    width: 14px; height: 14px; border-radius: 50%; background: var(--white);
  }
  .back-name {
    font-size: 26px; letter-spacing: 3px; color: var(--white); font-weight: 400;
  }
</style>
</head>
<body>
<main class="sheet">
  <section class="card card-front" aria-label="Business card front">
    <div class="front-band"></div>
    <span class="social-square" aria-hidden="true"></span>
    <div class="agent">
      <h1 class="agent-name">Olivia Hartley</h1>
      <p class="agent-title">Senior Property Consultant</p>
    </div>
    <div class="brand-seal">
      <span class="brand-seal-name">VORENDA<br>REALTY</span>
    </div>
    <address class="office-address">
      7C, 48 Harbour Road<br>
      Eastwood Bay, NSW 2199
    </address>
    <ul class="contact-list">
      <li>
        <svg class="contact-icon-svg" width="14" height="14" viewBox="0 0 14 14" aria-hidden="true">
          <circle cx="7" cy="7" r="7" fill="#ffffff" opacity=".85"/>
          <path d="M4.6 3.6c.4-.3.8-.2 1 .2l.6 1.1c.2.3.1.7-.2.9l-.4.3c.4.9 1.1 1.6 2 2l.3-.4c.2-.3.6-.4.9-.2l1.1.6c.4.2.5.6.2 1-.6.9-1.5 1.1-2.5.6-1.6-.8-2.8-2-3.6-3.6-.5-1-.3-1.9.6-2.5z" fill="#b39a6a"/>
        </svg>
        0400 517 293
      </li>
      <li><span class="contact-icon"></span>www.vorendarealty.com.au</li>
    </ul>
  </section>

  <section class="card card-back" aria-label="Business card back">
    <span class="back-mark" aria-hidden="true"></span>
    <h2 class="back-name">VORENDA REALTY</h2>
  </section>
</main>
</body>
</html>
```